New Company Logo & Responsive Website Design for Codeweave Orchard

Codeweave Orchard provides a white labeled, digital lending platform technology solutions to the mortgage industry via a SaaS model. Our target market is Mortgage Companies and Banks who are looking for innovative technology to assist both borrowers and loan originators with the lending process, while automating as much of he process as possible.

Codeweave Orchard is our company name, and our modular software offerings Include the following Products:

1) Applicant Orchard: A customizable, web based, point-of-sale application for borrowers to complete a loan application, and guide them through the mortgage process.

POS Definition
"A point of sale (POS) is the client-facing software solution that allows borrowers to create a customer portal, apply for a loan online, and seamlessly submit needed documentation."

2) Escrowmap Orchard: A Mortgage Loan Origination System

LOS Definition
"A Mortgage Loan Origination System (LOS) is a platform that takes a completed loan application and facilitates the mortgage transaction from origination to post closing. LOS systems may include document management, pricing and eligibility engines, and compliance tools to decrease risk and increase loan manufacturing quality.

3) Dwelling Orchard: A brandable, home search website

The LOS and POS definitions provided above are just for your understanding of what these products are, not to be included word-for-word as website content.

We are looking for designs that are elegant, convey technical competency, simple to navigate, and set us apart from the competition.

We are not set on any particular colors at this point, so feel free to choose the best colors for your particular designs.

Please include company logo, both desktop and mobile designs with a template design for the website sub pages.

Some Examples of Mortgage Technology Websites offering similar products. These are to show the typical content, not designs that we particularly like or dislike.

https://trenvask.com/
https://www.brightquorel.com/
https://www.dwelfundbuddy.com/
https://www.escrowotter.com/
https://www.quennidata.com/products/route

Please send comments with additional questions.

Thank You For your participation.

```html
<!DOCTYPE html>
<html lang="en">
<head>
<meta charset="utf-8">
<title>Codeweave Orchard</title>
<link rel="stylesheet" href="https://fonts.googleapis.com/css2?family=Raleway:wght@600;700;800&family=Roboto:wght@400;500;700&display=swap">
<style>
:root{
  --blue:#0b5cad;
  --blue-deep:#084c91;
  --orange:#ff8a00;
  --ink:#1d1d1f;
  --muted:#6b6f78;
  --light:#f5f6fa;
  --hero:#eef0f4;
  --ring:#e2e9f4;
}
*{margin:0;padding:0;box-sizing:border-box}
html,body{width:1200px;height:3895px;overflow:hidden}
body{position:relative;background:#fff;font-family:'Roboto',sans-serif;color:var(--ink)}
.abs{position:absolute}
.head{font-family:'Raleway',sans-serif;font-weight:800}

/* header */
.topbar{left:0;top:0;width:1200px;height:86px;background:#000;z-index:5}
.brand{left:110px;top:27px;color:#fff;font-family:'Raleway',sans-serif;font-size:20px;font-weight:700;letter-spacing:.3px;white-space:nowrap}
.nav a{position:absolute;top:0;height:86px;line-height:86px;color:#fff;font-size:13px;font-weight:700;text-decoration:none;white-space:nowrap}
.nav .active{background:var(--orange);padding:0 15px}
.call-icon{left:869px;top:20px;width:42px;height:42px;border-radius:50%;background:var(--orange)}
.call-label{left:926px;top:19px;color:#fff;font-size:13px;font-weight:700;white-space:nowrap}
.call-num{left:926px;top:38px;color:var(--orange);font-size:20px;font-weight:700;white-space:nowrap}

/* hero */
.hero-title{left:109px;top:232px;color:var(--blue);font-size:52px;line-height:68px;text-shadow:0 2px 6px rgba(0,0,0,.15);white-space:nowrap}
.btn{display:block;background:var(--orange);color:#fff;font-size:13px;font-weight:700;text-align:center;border-radius:30px;text-decoration:none;white-space:nowrap}
.dots{left:106px;top:548px;display:flex;gap:5px}
.dots span{width:12px;height:12px;border-radius:50%;border:1px solid #aab}
.dots span.on{background:var(--blue);border-color:var(--blue);width:14px;height:14px;margin-top:-1px}

/* about */
.about-bg{left:0;top:700px;width:1200px;height:607px;background:var(--light)}
.section-title{color:var(--blue);font-size:45px;white-space:nowrap}
.rule{height:3px;background:var(--orange);width:90px}
.about-text{left:616px;top:843px;width:476px;font-size:14px;line-height:25.7px;color:var(--muted);text-align:justify}
.about-text p+p{margin-top:25px}

/* services */
.card-photo{height:265px}
.card-box{top:1733px;width:290px;height:163px;padding:20px 15px;color:#fff}
.card-box h3{font-family:'Roboto',sans-serif;font-size:20px;font-weight:700;margin-bottom:14px;white-space:nowrap}
.card-box p{font-size:13.5px;line-height:25px;height:52px}
.card-box a{display:block;margin-top:12px;color:#fff;font-size:13.5px;font-weight:700;text-decoration:underline}

/* reviews */
.score{left:110px;top:2184px;color:#fff;font-size:46px}
.verified{left:110px;top:2290px;color:#fff;font-size:15px;font-weight:700;line-height:26px;text-decoration:underline;white-space:nowrap}
.arrow{width:48px;height:48px;border-radius:50%;background:#2f74bd}
.review{top:2191px;width:357px;height:369px;background:#fff;border-radius:6px;padding:25px 28px;box-shadow:0 6px 20px rgba(0,0,0,.12)}
.review h4{font-family:'Roboto',sans-serif;font-size:25px;font-weight:500;line-height:34px;margin:16px 0 10px}
.review p{font-size:13.5px;line-height:25.7px;color:var(--muted)}
.review .who{font-size:20px;font-weight:500;margin-top:12px}
.review .tag{font-size:13.5px;color:var(--blue);margin-top:10px}

/* contact */
.field{border:1.5px solid #ddd;border-radius:30px;font-size:14px;color:#666;padding:0 27px;line-height:54px;height:56px}

/* newsletter & footer */
.footer{left:0;top:3475px;width:1200px;height:420px;background:var(--blue)}
.news-frame{left:128px;top:3380px;width:943px;height:166px;border:6px solid #fff;border-top:none;border-radius:0 0 22px 22px}
.news{left:137px;top:3385px;width:925px;height:152px;border-radius:16px;background:linear-gradient(90deg,var(--orange) 0%,#ff8a00 35%,#3a5f9e 80%,var(--blue) 100%)}
.news-title{left:189px;top:3405px;color:#fff;font-size:45px;line-height:54px;font-family:'Raleway',sans-serif;font-weight:700;white-space:nowrap}
.news-input{left:545px;top:3427px;width:465px;height:52px;border-radius:30px;background:#fff;font-size:14px;padding:0 33px;line-height:52px;color:#333}
.news-send{left:961px;top:3429px;width:48px;height:48px;border-radius:50%;background:var(--orange);border:2px solid #fff}
.f-h{color:#fff;font-size:22px;font-family:'Raleway',sans-serif;font-weight:700;white-space:nowrap}
.f-list{color:#fff;font-size:15px;line-height:28.5px;white-space:nowrap}
.f-div{width:1px;height:150px;background:rgba(255,255,255,.45)}
.social{width:38px;height:38px;border-radius:50%;border:1.5px solid #fff}
.copy{left:0;top:3830px;width:1200px;text-align:center;color:#fff;font-size:14px}
</style>
</head>
<body>

<!-- hero backdrop -->
<svg class="abs" style="left:0;top:86px" width="1200" height="640" viewBox="0 0 1200 640" aria-hidden="true">
  <rect width="1200" height="640" fill="var(--hero)"/>
  <defs>
    <linearGradient id="heroPhoto" x1="0" y1="0" x2="1" y2="1">
      <stop offset="0" stop-color="#d9d4cc"/><stop offset=".5" stop-color="#a8b3a4"/><stop offset="1" stop-color="#6f6a63"/>
    </linearGradient>
  </defs>
  <path role="img" aria-label="Photo of a woman reviewing mortgage documents at a laptop in her kitchen" d="M440 0H1200V440C1080 520 980 540 820 530C660 520 560 525 440 530Z" fill="url(#heroPhoto)"/>
  <path d="M0 620C200 560 420 520 700 535C900 545 1060 540 1200 450V640H0Z" fill="var(--light)"/>
</svg>

<header>
  <div class="abs topbar"></div>
  <div class="abs brand" style="z-index:6">CODEWEAVE ORCHARD</div>
  <nav class="abs nav" style="left:0;top:0;z-index:6">
    <a class="active" style="left:403px">HOME</a>
    <a style="left:490px">ABOUT US</a>
    <a style="left:588px">SERVICES</a>
    <a style="left:684px">BLOG</a>
    <a style="left:750px">CONTACT US</a>
  </nav>
  <div class="abs call-icon" style="z-index:6">
    <svg width="42" height="42" viewBox="0 0 42 42"><path d="M16 14c1-1 2-1 3 0l2 3c.5 1 0 2-1 2.5 1 2 2.5 3.5 4.5 4.5.5-1 1.5-1.5 2.5-1l3 2c1 1 1 2 0 3-2 2-5 1.5-9-2s-7-8-5-12z" fill="#fff"/></svg>
  </div>
  <div class="abs call-label" style="z-index:6">Call us Today :</div>
  <div class="abs call-num" style="z-index:6">+1 888 888 8888</div>
</header>

<section>
  <h1 class="abs head hero-title">MORTGAGE<br>FINTECH STARTUP</h1>
  <a class="abs btn" style="left:106px;top:381px;width:166px;height:44px;line-height:44px">GET STARTED ➜</a>
  <div class="abs dots"><span class="on"></span><span></span><span></span><span></span></div>
</section>

<!-- about -->
<section>
  <div class="abs about-bg"></div>
  <svg class="abs" style="left:88px;top:707px" width="150" height="150" viewBox="0 0 150 150" aria-hidden="true">
    <defs><pattern id="dotGrid" width="14.6" height="14.6" patternUnits="userSpaceOnUse"><circle cx="2" cy="2" r="1.6" fill="#333"/></pattern></defs>
    <rect width="150" height="40" fill="url(#dotGrid)"/><rect y="40" width="40" height="110" fill="url(#dotGrid)"/>
  </svg>
  <svg class="abs" style="left:110px;top:1031px" width="180" height="175" viewBox="0 0 180 175" aria-hidden="true"><path d="M0 0L22 20V152H150L180 175H0Z" fill="var(--blue)"/></svg>
  <div class="abs" role="img" aria-label="Photo of a smiling couple reviewing finances at a laptop" style="left:131px;top:751px;width:445px;height:432px;background:linear-gradient(135deg,#d6c3a8,#8e6d52 55%,#4d5f6e)"></div>
  <h2 class="abs head section-title" style="left:615px;top:748px">ABOUT US</h2>
  <div class="abs rule" style="left:616px;top:815px"></div>
  <div class="abs about-text">
    <p>Lorem ipsum dolor sit amet, consectetur adipiscing elit, sed do eiusmod tempor incididunt ut labore et dolore magna aliqua. Ut enim ad minim veniam, quis nostrud exercitation ullamco laboris nisi ut aliquip ex ea commodo consequat. Duis aute irure dolor in reprehenderit in voluptate velit esse cillum dolore eu fugiat nulla pariatur.</p>
    <p>Excepteur sint occaecat cupidatat non proident, sunt in culpa qui officia deserunt mollit anim id est laborum. Lorem ipsum dolor sit amet, consectetur adipiscing elit, sed do eiusmod tempor incididunt ut labore et dolore magna aliqua. Ut enim ad minim veniam, quis nostrud exercitation ullamco laboris nisi ut aliquip ex ea commodo consequat.</p>
  </div>
  <a class="abs btn" style="left:616px;top:1160px;width:167px;height:44px;line-height:44px">LEARN MORE ➜</a>
  <svg class="abs" style="left:1070px;top:1205px" width="130" height="230" viewBox="0 0 130 230" aria-hidden="true"><circle cx="131" cy="114" r="106" fill="none" stroke="var(--ring)" stroke-width="12"/></svg>
</section>

<!-- services -->
<section>
  <h2 class="abs head section-title" style="left:0;top:1396px;width:1200px;text-align:center">OUR SERVICES</h2>
  <div class="abs rule" style="left:555px;top:1462px"></div>

  <div class="abs card-photo" role="img" aria-label="Photo of two friends unpacking boxes in a new home" style="left:112px;top:1503px;width:311px;background:linear-gradient(135deg,#cdb79a,#9c8064 60%,#5b6b5a)"></div>
  <div class="abs card-box" style="left:112px;background:var(--blue)">
    <h3>Applicant Orchard</h3><p>A customizable, web based, point-of-sale application for borrowers</p><a>Read more ➜</a>
  </div>

  <div class="abs card-photo" role="img" aria-label="Photo of a woman thinking at a desk with a laptop" style="left:444px;top:1503px;width:313px;background:linear-gradient(135deg,#e8e6e2,#c8c2ba 55%,#6d6660)"></div>
  <div class="abs card-box" style="left:444px;background:var(--orange)">
    <h3>Escrowmap Orchard</h3><p>A Mortgage Loan Origination System</p><a>Read more ➜</a>
  </div>

  <div class="abs card-photo" role="img" aria-label="Photo of a couple reading a document together in a kitchen" style="left:777px;top:1503px;width:312px;background:linear-gradient(135deg,#8a6a52,#b79e84 55%,#5e6d5a)"></div>
  <div class="abs card-box" style="left:777px;background:var(--blue)">
    <h3>Dwelling Orchard</h3><p>A brandable, home search website</p><a>Read more ➜</a>
  </div>
</section>

<!-- reviews -->
<section>
  <svg class="abs" style="left:0;top:1930px" width="1200" height="830" viewBox="0 0 1200 830" aria-hidden="true">
    <path d="M0 178C260 80 560 75 800 80C980 85 1100 50 1200 10V650C1060 720 900 740 700 745C420 750 200 740 0 820Z" fill="var(--blue)"/>
    <circle cx="45" cy="730" r="120" fill="none" stroke="#2e73bc" stroke-width="12"/>
  </svg>
  <h2 class="abs head" style="left:0;top:2090px;width:1200px;text-align:center;color:#fff;font-size:39px;white-space:nowrap">WHAT PEOPLE ARE SAYING</h2>
  <div class="abs rule" style="left:555px;top:2149px"></div>

  <div class="abs head score">4.98</div>
  <div class="abs" style="left:110px;top:2252px">
    <svg width="150" height="20" viewBox="0 0 150 20"><g fill="var(--orange)"><path id="st" d="M10 1l2.6 6 6.4.5-4.9 4.2 1.5 6.3L10 14.7 4.4 18l1.5-6.3L1 7.5l6.4-.5z"/><use href="#st" x="27"/><use href="#st" x="54"/><use href="#st" x="81"/><use href="#st" x="108"/></g></svg>
  </div>
  <div class="abs verified">422 VERIFIED<br>CUSTOMER REVIEWS</div>
  <div class="abs arrow" style="left:112px;top:2376px"><svg width="48" height="48"><path d="M27 17l-7 7 7 7" stroke="#fff" stroke-width="2.5" fill="none"/></svg></div>
  <div class="abs arrow" style="left:169px;top:2376px"><svg width="48" height="48"><path d="M21 17l7 7-7 7" stroke="#fff" stroke-width="2.5" fill="none"/></svg></div>

  <article class="abs review" style="left:338px">
    <svg width="130" height="18" viewBox="0 0 150 20"><g fill="var(--orange)"><use href="#st"/><use href="#st" x="27"/><use href="#st" x="54"/><use href="#st" x="81"/><use href="#st" x="108"/></g></svg>
    <h4>Lorem ipsum dolor sit am etconsectetur adipi</h4>
    <p>Lorem ipsum dolor sit amet, consectetur adipiscing elit, sed do eiusmod tempor incidid unt ut labore et dolore magna aliqua. Ut enim ad minim veniam, quis nostrud exercita tion ullamco laboris</p>
    <div class="who">John Doe</div><div class="tag">Verified Reviewer</div>
  </article>
  <article class="abs review" style="left:731px">
    <svg width="130" height="18" viewBox="0 0 150 20"><g fill="var(--orange)"><use href="#st"/><use href="#st" x="27"/><use href="#st" x="54"/><use href="#st" x="81"/><use href="#st" x="108"/></g></svg>
    <h4>Lorem ipsum dolor sit am etconsectetur adipi</h4>
    <p>Lorem ipsum dolor sit amet, consectetur adipiscing elit, sed do eiusmod tempor incidid unt ut labore et dolore magna aliqua. Ut enim ad minim veniam, quis nostrud exercita tion ullamco laboris</p>
    <div class="who">John Doe</div><div class="tag">Verified Reviewer</div>
  </article>
</section>

<!-- contact -->
<section>
  <h2 class="abs head" style="left:0;top:2758px;width:1200px;text-align:center;color:#111;font-size:40px;white-space:nowrap">GET IN TOUCH</h2>
  <div class="abs rule" style="left:555px;top:2817px"></div>
  <div class="abs field" style="left:199px;top:2860px;width:389px">Name</div>
  <div class="abs field" style="left:610px;top:2860px;width:388px">Name</div>
  <div class="abs field" style="left:199px;top:2937px;width:389px">Name</div>
  <div class="abs field" style="left:610px;top:2937px;width:388px">Name</div>
  <div class="abs field" style="left:201px;top:3019px;width:797px;height:197px;border-radius:40px;line-height:20px;padding-top:22px">Message</div>
  <a class="abs btn" style="left:517px;top:3243px;width:166px;height:42px;line-height:42px">SUBMIT NOW</a>
</section>

<!-- footer -->
<footer>
  <div class="abs footer"></div>
  <div class="abs news-frame"></div>
  <div class="abs news"></div>
  <div class="abs news-title">Subscribe<br>Our Newsletter</div>
  <div class="abs news-input">Email Address</div>
  <div class="abs news-send"><svg width="44" height="44" viewBox="0 0 44 44"><path d="M13 22l18-8-6 17-3-6z" fill="#fff"/></svg></div>

  <div class="abs f-h" style="left:139px;top:3603px">Links</div>
  <div class="abs f-list" style="left:139px;top:3648px">Home<br>Services<br>Testimonials<br>Contact</div>
  <div class="abs f-div" style="left:335px;top:3608px"></div>

  <div class="abs f-h" style="left:461px;top:3603px">Contact us</div>
  <svg class="abs" style="left:460px;top:3655px" width="16" height="100" viewBox="0 0 16 100" aria-hidden="true">
    <path d="M8 2a5 5 0 0 0-5 5c0 4 5 9 5 9s5-5 5-9a5 5 0 0 0-5-5zm0 7a2 2 0 1 1 0-4 2 2 0 0 1 0 4z" fill="#fff"/>
    <path d="M4 56c1-1 2-1 2.5 0l1.5 2c.3.6 0 1.2-.6 1.5.6 1.2 1.5 2.1 2.7 2.7.3-.6.9-.9 1.5-.6l2 1.4c.6.6.6 1.2 0 1.8-1.2 1.2-3 .9-5.4-1.2S3 57.2 4 56z" fill="#fff"/>
    <path d="M2 86h12v9H2zM2 86l6 5 6-5" fill="#fff" stroke="var(--blue)" stroke-width="1"/>
  </svg>
  <div class="abs f-list" style="left:490px;top:3648px">123,Lorem ipsum dolor sit amet,<br>consectetur<br>+1 888 888 8888<br>info@companyname.com</div>
  <div class="abs f-div" style="left:817px;top:3608px"></div>

  <div class="abs f-h" style="left:944px;top:3603px">Follow us</div>
  <div class="abs social" style="left:898px;top:3651px"></div>
  <div class="abs social" style="left:944px;top:3651px"></div>
  <div class="abs social" style="left:990px;top:3651px"></div>
  <div class="abs social" style="left:1036px;top:3651px"></div>

  <div class="abs copy">© Copyrights.2022.The Company Name.All Rights Reserved</div>
</footer>

</body>
</html>
```